Brindlow Electrical Solutions needs a website

We need a new website designed because our current one is outdated. I would like a one-page website. We are a B2B company and want to maintain a professional appearance to appeal to project managers and directors.

for some reference, these are a few of my competitor's websites; we offer the same services.

https://valtorwiring.com.au/services
https://www.dunsary.com.au/mechanical-electrical-services/
https://www.gravik.com.au/

Industry/Entity Type

Electrical

Number of Pages Required

1 page

Font styles to use
Sans Serif

Colors
0054AA
0677BA
7BADD7
CADEEF
E8F1F8

```html
<!DOCTYPE html>
<html lang="en">
<head>
<meta charset="utf-8">
<title>Brindlow Electrical Solutions</title>
<link href="https://fonts.googleapis.com/css2?family=Roboto:wght@400;500;700&display=swap" rel="stylesheet">
<style>
:root{
  --navy:#0054AA;
  --blue:#0677BA;
  --sky:#7BADD7;
  --mist:#CADEEF;
  --ice:#E8F1F8;
  --ink:#1b1b1b;
  --text:#333;
  --white:#fff;
}
*{box-sizing:border-box;margin:0;padding:0}
html,body{width:1200px;height:3559px;overflow:hidden}
body{font-family:"Roboto",Arial,sans-serif;color:var(--text);background:var(--white);position:relative}
section,header,footer,div,span,a,p,h1,h2,h3{position:relative}
.abs{position:absolute}
a{text-decoration:none;color:inherit}

/* top bar */
.topbar{height:30px;background:var(--navy);color:var(--white);font-size:11px}
.dot-ico{position:absolute;width:17px;height:17px;border-radius:50%;background:var(--white);top:6px}
.top-contact{position:absolute;top:0;height:30px;display:flex;align-items:center;gap:6px}
.top-contact .dot-ico{position:static}
.top-contact svg{display:block}

/* header */
.site-header{height:70px;background:var(--white)}
.brand{position:absolute;left:64px;top:11px;display:flex;align-items:center;gap:10px}
.brand-mark{width:46px;height:46px;border-radius:50%;background:var(--navy)}
.brand-name{font-size:24px;font-weight:700;color:var(--navy);letter-spacing:1px;line-height:1}
.brand-sub{font-size:10px;font-weight:700;color:var(--navy);letter-spacing:1.4px}
.nav a{position:absolute;top:24px;font-size:17px;color:var(--ink)}
.nav a.active{color:var(--blue);font-weight:500}
.nav a.active::after{content:"";position:absolute;left:-6px;right:-6px;top:44px;height:2px;background:var(--blue)}
.nav .caret{font-size:10px;margin-left:3px}
.hdr-btn{position:absolute;top:26px;width:17px;height:17px;border-radius:50%;background:var(--navy)}

/* hero */
.hero{height:519px;background:linear-gradient(90deg,#1d2126 0%,#2a3138 40%,#4b5a66 70%,#6a7a88 100%)}
.hero h1{position:absolute;left:62px;top:254px;width:700px;color:var(--white);font-size:42px;font-weight:500;line-height:52px}
.hero p{position:absolute;left:62px;top:372px;width:660px;color:var(--white);font-size:14px;line-height:17px}
.btn{display:flex;align-items:center;justify-content:center;background:var(--navy);color:var(--white);font-size:17px;font-weight:500}
.hero .btn{position:absolute;left:62px;top:430px;width:210px;height:32px}
.slider-dots{position:absolute;display:flex;gap:13px;align-items:center}
.slider-dots i{width:7px;height:7px;border-radius:50%;background:var(--blue);display:block}
.slider-dots i.on{background:var(--white);box-shadow:0 0 0 2px var(--blue)}

/* features */
.features{height:213px;background:var(--blue)}
.feature{position:absolute;top:51px;width:343px;height:110px;background:var(--white);display:flex;align-items:center;padding-left:40px;gap:14px}
.feature h3{font-size:17px;font-weight:500;color:var(--blue);margin-bottom:6px}
.feature p{font-size:14px;line-height:17px;color:var(--text)}

/* about */
.about{height:609px}
.about h2{position:absolute;left:66px;top:150px;font-size:47px;font-weight:700;color:var(--ink)}
.about .lead{position:absolute;left:62px;top:216px;width:525px;font-size:14px;line-height:17px}
.stat{position:absolute;top:295px}
.stat b{display:block;font-size:37px;font-weight:500;color:var(--navy);line-height:44px}
.stat span{font-size:17px;font-weight:500;color:var(--ink)}
.stat-rule{position:absolute;left:244px;top:295px;width:2px;height:64px;background:var(--blue)}
.about .note{position:absolute;left:62px;top:370px;width:525px;font-size:14px;line-height:17px}
.about .btn{position:absolute;left:62px;top:426px;width:210px;height:32px}
.tile{position:absolute;width:258px}
.tile-blue{background:var(--navy);color:var(--white)}
.tile-blue.count{top:63px;left:606px;height:124px;text-align:center;padding-top:26px}
.count b{display:block;font-size:37px;font-weight:500;line-height:42px}
.count span{font-size:17px;font-weight:500}
.photo-city{left:606px;top:204px;height:342px;background:linear-gradient(180deg,#5d5a78 0%,#8e6a6a 45%,#c98a5a 62%,#2b2a36 100%)}
.play{position:absolute;left:93px;top:135px;width:72px;height:72px;border-radius:50%;background:rgba(120,120,130,.7);display:flex;align-items:center;justify-content:center}
.play i{width:38px;height:38px;border-radius:50%;background:var(--white);display:flex;align-items:center;justify-content:center}
.photo-panel{left:880px;top:63px;height:342px;background:linear-gradient(160deg,#8a96a4 0%,#4e5966 50%,#2a2f36 100%)}
.tile-blue.years{left:880px;top:422px;height:124px;display:flex;align-items:center;justify-content:center;gap:10px}
.years b{font-size:37px;font-weight:500}
.years span{font-size:17px;font-weight:500;line-height:20px}

/* services */
.services{height:739px;background:var(--ice)}
.sec-title{position:absolute;left:0;width:1200px;text-align:center;font-size:47px;font-weight:700;color:var(--ink)}
.sec-lead{position:absolute;left:300px;width:600px;text-align:center;font-size:14px;line-height:17px}
.services .sec-title{top:50px}
.services .sec-lead{top:129px}
.svc{position:absolute;width:326px;height:210px;background:var(--white);box-shadow:0 0 4px rgba(0,0,0,.15);text-align:center}
.svc svg{position:absolute;left:123px;top:42px}
.svc h3{position:absolute;left:0;right:0;top:150px;font-size:17px;font-weight:500;color:var(--ink)}
.svc::after{content:"";position:absolute;left:87px;width:152px;bottom:0;height:2px;background:var(--blue)}
.svc.active{background:linear-gradient(135deg,#3f82bf 0%,#1f6fb2 50%,#2b79b8 100%)}
.svc.active h3{color:var(--white)}
.svc.active::after{display:none}

/* works */
.works{height:665px}
.works .sec-title{top:64px}
.works .sec-lead{top:137px}
.tab{position:absolute;top:188px;width:154px;height:33px;border:1px solid var(--mist);display:flex;align-items:center;justify-content:center;font-size:17px;font-weight:500;color:var(--blue);background:var(--white);box-shadow:0 1px 3px rgba(0,0,0,.12)}
.tab.on{background:var(--navy);color:var(--white);border-color:var(--navy)}
.work{position:absolute;top:246px;width:323px;height:318px;box-shadow:0 0 4px rgba(0,0,0,.2)}
.work-1{left:58px;background:linear-gradient(110deg,#d7dadd 0%,#b8c0c8 45%,#eef0f2 100%)}
.work-2{left:435px;background:linear-gradient(160deg,#2c7fb9 0%,#1f6fa9 100%);color:var(--white);text-align:center}
.work-3{left:811px;background:linear-gradient(180deg,#9fb3c4 0%,#6a7c86 50%,#3d4a4f 100%)}
.work-2 h3{margin-top:124px;font-size:17px;font-weight:500}
.work-2 p{margin:6px auto 0;width:270px;font-size:14px;line-height:17px}
.work-2 a{display:inline-block;margin-top:5px;font-size:14px;text-decoration:underline}

/* quote */
.quote{height:362px;background:linear-gradient(180deg,#1c3a56 0%,#2f5878 45%,#41657e 100%)}
.quote .sec-title{top:32px;color:var(--white)}
.quote .sec-lead{top:101px;color:var(--white)}
.field{position:absolute;width:347px;height:50px;background:var(--white);border-radius:2px;font-size:14px;color:#444;display:flex;align-items:center;padding:0 16px;justify-content:space-between}
.quote .btn{position:absolute;left:496px;top:301px;width:208px;height:30px}

/* footer */
.site-footer{height:352px;background:var(--navy);color:var(--white)}
.foot-brand{position:absolute;left:64px;top:66px;display:flex;align-items:center;gap:10px}
.foot-brand .brand-mark{background:var(--white)}
.foot-brand .brand-name,.foot-brand .brand-sub{color:var(--white)}
.foot-about{position:absolute;left:62px;top:160px;width:420px;font-size:14px;line-height:17px}
.foot-col{position:absolute;top:70px}
.foot-col h4{font-size:21px;font-weight:500;margin-bottom:16px}
.foot-col li{list-style:none;font-size:14px;height:33px}
.contact-item{display:flex;align-items:center;gap:10px;font-size:14px;height:41px}
.c-ico{width:23px;height:23px;border-radius:50%;background:var(--white);display:flex;align-items:center;justify-content:center}
.foot-rule{position:absolute;left:0;right:0;top:291px;height:1px;background:rgba(255,255,255,.5)}
.copyright{position:absolute;left:62px;top:313px;font-size:14px}
.soc{position:absolute;top:310px;width:25px;height:25px;border-radius:50%;background:var(--white)}
</style>
</head>
<body>

<div class="topbar">
  <span class="dot-ico" style="left:64px"></span>
  <span class="dot-ico" style="left:102px"></span>
  <span class="dot-ico" style="left:140px"></span>
  <div class="top-contact" style="left:696px"><span class="dot-ico"><svg width="17" height="17" viewBox="0 0 17 17"><path d="M6 5l1.5 2-1 1a5 5 0 0 0 2.5 2.5l1-1 2 1.5-1 1.5C8 12 5 9 4.8 6z" fill="#0054AA"/></svg></span>02 9460 2731</div>
  <div class="top-contact" style="left:805px"><span class="dot-ico"><svg width="17" height="17" viewBox="0 0 17 17"><path d="M8.5 4a3 3 0 0 0-3 3c0 2 3 6 3 6s3-4 3-6a3 3 0 0 0-3-3z" fill="#0054AA"/></svg></span>Sydney NSW, Australia</div>
  <div class="top-contact" style="left:956px"><span class="dot-ico"><svg width="17" height="17" viewBox="0 0 17 17"><rect x="4.5" y="5.5" width="8" height="6" fill="none" stroke="#0054AA"/><path d="M4.5 5.5l4 3 4-3" fill="none" stroke="#0054AA"/></svg></span>info@brindlowelectrical.com.au</div>
</div>

<header class="site-header">
  <div class="brand">
    <span class="brand-mark"></span>
    <div><div class="brand-name">BRINDLOW</div><div class="brand-sub">ELECTRICAL SOLUTIONS</div></div>
  </div>
  <nav class="nav">
    <a class="active" style="left:472px">Home</a>
    <a style="left:558px">About Us<span class="caret">&#8964;</span></a>
    <a style="left:678px">Services<span class="caret">&#8964;</span></a>
    <a style="left:797px">Latest Projects<span class="caret">&#8964;</span></a>
    <a style="left:964px">Contact Us</a>
  </nav>
  <span class="hdr-btn" style="left:1088px"></span>
  <span class="hdr-btn" style="left:1119px"></span>
</header>

<section class="hero" role="img" aria-label="Electrician in hard hat and blue workwear standing in front of an open switchboard">
  <h1>Your Trusted Partner for Safe and Reliable Electrical Solutions</h1>
  <p>Lorem ipsum dolor sit amet, consectetur adipiscing elit, sed do eiusmod tempor incididunt ut labore et dolore magna aliqua.</p>
  <a class="btn">Get a Free Quote</a>
  <div class="slider-dots" style="left:577px;top:590px"><i class="on"></i><i></i><i></i></div>
</section>

<section class="features">
  <div class="feature" style="left:62px">
    <svg width="70" height="52" viewBox="0 0 70 52" fill="none" stroke="#0677BA" stroke-width="2"><rect x="3" y="4" width="64" height="44" rx="3"/><rect x="10" y="14" width="16" height="18"/><circle cx="18" cy="20" r="3"/><path d="M12 30c2-5 10-5 12 0"/><path d="M32 18h28M32 24h22M32 30h26M40 40h20"/></svg>
    <div><h3>Licensed Electricians</h3><p>Lorem ipsum dolor sit amet, consectetur adipiscing</p></div>
  </div>
  <div class="feature" style="left:429px">
    <svg width="64" height="64" viewBox="0 0 64 64" fill="none" stroke="#0677BA" stroke-width="2.5"><path d="M56 24A26 26 0 1 0 58 36" stroke-dasharray="5 3"/><path d="M52 16l4 8 8-3"/><text x="12" y="39" font-family="Roboto,sans-serif" font-size="20" font-weight="700" fill="#0677BA" stroke="none">24/7</text></svg>
    <div><h3>24/7 Support</h3><p>Lorem ipsum dolor sit amet, consectetur adipiscing</p></div>
  </div>
  <div class="feature" style="left:795px">
    <svg width="62" height="64" viewBox="0 0 62 64" fill="none" stroke="#1b1b1b" stroke-width="2"><rect x="6" y="3" width="36" height="50" rx="2"/><rect x="12" y="9" width="20" height="10"/><path d="M12 26h24M12 33h20M12 40h14"/><path d="M44 34l10 4v8c0 7-5 11-10 13-5-2-10-6-10-13v-8z" fill="#fff"/><path d="M39 46l4 4 7-8"/></svg>
    <div><h3>Quality Assurance</h3><p>Lorem ipsum dolor sit amet, consectetur adipiscing</p></div>
  </div>
</section>

<section class="about">
  <h2>About Us</h2>
  <p class="lead">Lorem ipsum dolor sit amet, consectetur adipiscing elit, sed do eiusmod tempor incididunt ut labore et dolore magna aliqua. Ut enim ad minim veniam, quis nostrud exercitation ullamco laboris nisi ut aliquip ex ea commodo consequat.</p>
  <div class="stat" style="left:62px"><b>25K+</b><span>Happy Customers</span></div>
  <span class="stat-rule"></span>
  <div class="stat" style="left:279px"><b>99.9%</b><span>Good Ratings</span></div>
  <p class="note">Lorem ipsum dolor sit amet, consectetur adipiscing elit, sed do eiusmod tempor incididunt ut labore et dolore magna aliqua.</p>
  <a class="btn">Read More</a>

  <div class="tile tile-blue count"><b>45K+</b><span>Project Done</span></div>
  <div class="tile photo-city" role="img" aria-label="City skyline at dusk, video thumbnail">
    <span class="play"><i><svg width="12" height="12" viewBox="0 0 12 12"><path d="M3 1l8 5-8 5z" fill="#0054AA"/></svg></i></span>
  </div>
  <div class="tile photo-panel" role="img" aria-label="Gloved hand testing a switchboard with a clamp meter"></div>
  <div class="tile tile-blue years"><b>15+</b><span>Year of<br>Experiences</span></div>
</section>

<section class="services">
  <h2 class="sec-title">Our Service</h2>
  <p class="sec-lead">Lorem ipsum dolor sit amet, consectetur adipiscing elit, sed do eiusmod tempor incididunt ut labore et dolore magna aliqua.</p>

  <div class="svc" style="left:62px;top:179px">
    <svg width="80" height="80" viewBox="0 0 80 80" fill="none"><circle cx="34" cy="40" r="22" stroke="#1b1b1b" stroke-width="6" stroke-dasharray="6 4"/><circle cx="34" cy="40" r="14" fill="#0677BA"/><circle cx="34" cy="40" r="6" fill="#fff"/><circle cx="66" cy="40" r="9" stroke="#0677BA" stroke-width="4"/><path d="M48 40h10" stroke="#1b1b1b" stroke-width="4"/></svg>
    <h3>Mechanical Electrical Services</h3>
  </div>
  <div class="svc active" style="left:446px;top:179px" role="img" aria-label="Engineers in hard hats reviewing plans, blue overlay">
    <svg width="80" height="80" viewBox="0 0 80 80" fill="none" stroke="#fff" stroke-width="3"><rect x="8" y="26" width="26" height="50"/><path d="M14 34h6M24 34h6M14 44h6M24 44h6M14 54h6M24 54h6"/><rect x="38" y="50" width="20" height="26"/><circle cx="58" cy="22" r="16"/><path d="M58 12v20M52 18l6-6 6 6"/></svg>
    <h3>Building Management System</h3>
  </div>
  <div class="svc" style="left:812px;top:179px">
    <svg width="80" height="86" viewBox="0 0 80 86" fill="none"><rect x="10" y="4" width="60" height="76" rx="6" stroke="#0677BA" stroke-width="6"/><rect x="30" y="20" width="20" height="44" rx="10" stroke="#1b1b1b" stroke-width="3"/><rect x="32" y="42" width="16" height="20" rx="6" fill="#0677BA"/></svg>
    <h3>Switchboard Design &amp; Installation</h3>
  </div>
  <div class="svc" style="left:62px;top:437px">
    <svg width="80" height="86" viewBox="0 0 80 86" fill="none" stroke-width="4"><path d="M12 80V24h28v56" stroke="#0677BA"/><path d="M20 32v40M28 32v40M34 32v40" stroke="#1b1b1b" stroke-width="3"/><path d="M40 12v72M40 12a30 30 0 0 1 0 60" stroke="#0677BA"/><path d="M4 82h52" stroke="#0677BA"/></svg>
    <h3>Commercial &amp; Industrial Projects</h3>
  </div>
  <div class="svc" style="left:437px;top:437px">
    <svg width="84" height="86" viewBox="0 0 84 86" fill="none" stroke-width="3"><rect x="20" y="4" width="48" height="44" stroke="#1b1b1b"/><path d="M26 16l3 3 5-6M26 28l3 3 5-6M38 16h22M38 28h22M38 40h16" stroke="#1b1b1b"/><path d="M6 54l16-8 14 10 16-4 22 12-18 16-20-10-16 4z" stroke="#0677BA"/></svg>
    <h3>Project Management</h3>
  </div>
  <div class="svc" style="left:812px;top:437px">
    <svg width="80" height="86" viewBox="0 0 80 86" fill="none"><path d="M10 34a30 30 0 0 1 60 0z" fill="#1b1b1b"/><rect x="6" y="34" width="68" height="8" fill="#0677BA"/><circle cx="40" cy="58" r="20" stroke="#0677BA" stroke-width="8" stroke-dasharray="7 4"/><circle cx="40" cy="58" r="8" fill="#fff" stroke="#0677BA" stroke-width="3"/></svg>
    <h3>Engineering</h3>
  </div>
  <div class="slider-dots" style="left:577px;top:675px"><i class="on"></i><i></i><i></i></div>
</section>

<section class="works">
  <h2 class="sec-title">Our Recent Works</h2>
  <p class="sec-lead">Lorem ipsum dolor sit amet, consectetur adipiscing elit, sed do eiusmod tempor incididunt ut labore et dolore magna aliqua.</p>
  <span class="tab on" style="left:228px">All</span>
  <span class="tab" style="left:421px">Commercial</span>
  <span class="tab" style="left:616px">Residential</span>
  <span class="tab" style="left:809px">Industrial</span>
  <div class="work work-1" role="img" aria-label="Electrician in hard hat working on a ceiling fitting"></div>
  <div class="work work-2" role="img" aria-label="Aerial view of a residential suburb with blue overlay">
    <h3>Residential Electrical Works</h3>
    <p>Lorem ipsum dolor sit amet, consectetur adipiscing elit.</p>
    <a>Read More</a>
  </div>
  <div class="work work-3" role="img" aria-label="Engineers in hard hats reviewing a laptop in an industrial plant"></div>
  <div class="slider-dots" style="left:573px;top:592px"><i class="on"></i><i></i><i></i></div>
</section>

<section class="quote" role="img" aria-label="Aerial view of a harbour city skyline behind the quote form">
  <h2 class="sec-title">Request A Quote</h2>
  <p class="sec-lead">Lorem ipsum dolor sit amet, consectetur adipiscing elit, sed do eiusmod tempor incididunt ut labore et dolore magna aliqua.</p>
  <span class="field" style="left:62px;top:148px">Your Name</span>
  <span class="field" style="left:427px;top:148px">Email ID</span>
  <span class="field" style="left:790px;top:148px">Address</span>
  <span class="field" style="left:62px;top:230px">Select Your Work Type<span>&#8964;</span></span>
  <span class="field" style="left:427px;top:230px">Selected Date<span>&#8964;</span></span>
  <span class="field" style="left:790px;top:230px">Phone Number</span>
  <a class="btn">Submit</a>
</section>

<footer class="site-footer">
  <div class="foot-brand">
    <span class="brand-mark"></span>
    <div><div class="brand-name" style="font-size:30px">BRINDLOW</div><div class="brand-sub" style="font-size:12px">ELECTRICAL SOLUTIONS</div></div>
  </div>
  <p class="foot-about">Lorem ipsum dolor sit amet, consectetur adipiscing elit, sed do eiusmod tempor</p>
  <div class="foot-col" style="left:522px"><h4>Explore</h4><ul><li>Home</li><li>About Us</li><li>Service</li><li>Latest Project</li></ul></div>
  <div class="foot-col" style="left:700px"><h4>Quick Links</h4><ul><li>Pricing</li><li>Blog</li><li>FAQ</li><li>Testimonial</li></ul></div>
  <div class="foot-col" style="left:903px"><h4>Contact Info</h4>
    <div class="contact-item"><span class="c-ico"><svg width="14" height="14" viewBox="0 0 14 14"><path d="M3 2l2 2.5-1 1.2a6 6 0 0 0 3.3 3.3l1.2-1L11 10l-1.2 1.8C6 11 3 8 2.4 3.6z" fill="#0054AA"/></svg></span>02 9460 2731</div>
    <div class="contact-item"><span class="c-ico"><svg width="14" height="14" viewBox="0 0 14 14"><path d="M7 2a3.2 3.2 0 0 0-3.2 3.2C3.8 7.5 7 12 7 12s3.2-4.5 3.2-6.8A3.2 3.2 0 0 0 7 2z" fill="#0054AA"/></svg></span>Sydney NSW, Australia</div>
    <div class="contact-item"><span class="c-ico"><svg width="14" height="14" viewBox="0 0 14 14"><rect x="2" y="3.5" width="10" height="7" fill="none" stroke="#0054AA" stroke-width="1.3"/><path d="M2 3.5l5 4 5-4" fill="none" stroke="#0054AA" stroke-width="1.3"/></svg></span>info@brindlowelectrical.com.au</div>
  </div>
  <span class="foot-rule"></span>
  <p class="copyright">&copy; Copyright 2021 Brindlow Electrical Solutions | All Rights Reserved</p>
  <span class="soc" style="left:1038px"></span>
  <span class="soc" style="left:1076px"></span>
  <span class="soc" style="left:1113px"></span>
</footer>

</body>
</html>
```